Sunny Paths and joy Business card

I have a logo, but will like a business card design. Is for a travel agency in Mexico. We focus in family experiences.

I will liek some thing different and unique, from the traditional business card, something to get remmeber for.

Business card information:

Leandro T. Ocampo
leandro@sunnypathsjoy.example

Alameda 482, 3 piso
Col. Tlalpizco
Mexico, D.F. 07320

office: (55) 5000-0142
mobile: (55) 9000-0187

www.sunnypathsjoy.example
@sunnypjoy
blog: sunnypathsandjoy.blogsite.example
facebook: SunnyPathsAndJoy

```html
<!DOCTYPE html>
<html lang="es">
<head>
<meta charset="utf-8">
<title>Sunny Paths and joy – Business card</title>
<link rel="stylesheet" href="https://fonts.googleapis.com/css2?family=Poppins:wght@400;600;700&display=swap">
<style>
  :root {
    --page: #e9eaec;
    --card: #ffffff;
    --brand-blue: #1f3fd0;
    --ink: #111111;
    --on-blue: #ffffff;
    --shadow: rgba(0, 0, 0, 0.18);
  }
  * { box-sizing: border-box; margin: 0; padding: 0; }
  html, body {
    width: 1200px; height: 800px; overflow: hidden;
    background: var(--page);
    font-family: "Poppins", sans-serif;
  }
  .canvas {
    position: relative; width: 1200px; height: 800px;
    display: flex; align-items: center; justify-content: center; gap: 50px;
  }
  .card {
    position: relative; width: 540px; height: 310px;
    background: var(--card);
    box-shadow: 0 6px 18px var(--shadow);
    overflow: hidden;
  }
  .card__band {
    position: absolute; left: 0; right: 0; bottom: 0;
    background: var(--brand-blue);
  }
  /* Contact side */
  .contact .card__band { height: 72px; }
  .contact__name {
    position: absolute; left: 30px; top: 28px;
    color: var(--brand-blue); font-weight: 700; font-size: 30px;
    letter-spacing: -0.5px; line-height: 1;
  }
  .contact__web {
    position: absolute; left: 30px; top: 64px;
    color: var(--ink); font-weight: 700; font-size: 19px; line-height: 1;
  }
  .contact__phones {
    position: absolute; left: 30px; top: 186px;
    color: var(--ink); font-weight: 600; font-size: 14px;
  }
  .contact__phones .num { color: var(--brand-blue); }
  .contact__address {
    position: absolute; left: 30px; top: 212px;
    color: var(--brand-blue); font-size: 11px; font-weight: 600;
  }
  .contact__lines {
    position: absolute; left: 30px; bottom: 14px;
    color: var(--on-blue); font-size: 10px; line-height: 1.7;
  }
  .contact__social {
    position: absolute; right: 22px; bottom: 14px;
    color: var(--on-blue); font-size: 10px; line-height: 1.7;
    list-style: none;
  }
  .contact__social li { display: flex; align-items: center; gap: 6px; }
  .social-square {
    width: 10px; height: 10px; background: var(--on-blue); display: inline-block;
  }
  /* Brand side */
  .brand .card__band { height: 52px; }
  .brand__mark {
    position: absolute; left: 0; right: 0; top: 100px;
    display: flex; align-items: center; justify-content: center; gap: 12px;
  }
  .brand__dot {
    width: 34px; height: 34px; border-radius: 50%; background: var(--brand-blue);
  }
  .brand__name {
    color: var(--brand-blue); font-weight: 700; font-size: 32px; line-height: 1;
  }
</style>
</head>
<body>
<main class="canvas">
  <section class="card contact" aria-label="Contact side">
    <h1 class="contact__name">Leandro T. Ocampo</h1>
    <p class="contact__web">www.sunnypathsjoy.example</p>
    <p class="contact__phones">office: <span class="num">(55) 5000-0142</span> mobile: <span class="num">(55) 9000-0187</span></p>
    <p class="contact__address">Alameda 482, 3 piso Col. Tlalpizco Mexico, D.F. 07320</p>
    <div class="card__band"></div>
    <p class="contact__lines">leandro@sunnypathsjoy.example<br>@sunnypjoy</p>
    <ul class="contact__social">
      <li><span class="social-square"></span>SunnyPathsAndJoy</li>
      <li><span class="social-square"></span>sunnypathsandjoy.blogsite.example</li>
    </ul>
  </section>

  <section class="card brand" aria-label="Brand side">
    <div class="brand__mark">
      <span class="brand__dot"></span>
      <span class="brand__name">Sunny Paths and joy</span>
    </div>
    <div class="card__band"></div>
  </section>
</main>
</body>
</html>
```